" Somos reconhecidos em nossa comunidade como um posto de serviços de excelência, que oferece ao nossos clientes um ambiente, produtos e atendimento superior ao dos nossos concorrentes. "

```html
<!DOCTYPE html>
<html lang="pt-BR">
<head>
<meta charset="utf-8">
<title>Vértice – Cartão de visita</title>
<link href="https://fonts.googleapis.com/css2?family=Montserrat:wght@300;400;600;700;800&display=swap" rel="stylesheet">
<style>
  :root {
    --backdrop: #3b4751;
    --card-dark: #4b5056;
    --card-light: #f3f3f1;
    --brand-red: #9e1b1e;
    --ink: #3d4248;
    --ink-soft: #7a7f85;
    --white: #ffffff;
  }
  * { box-sizing: border-box; margin: 0; padding: 0; }
  html, body {
    width: 1200px; height: 1200px; overflow: hidden;
    background: var(--backdrop);
    font-family: "Montserrat", sans-serif;
  }
  .sheet {
    width: 1200px; height: 1200px;
    display: flex; flex-direction: column; align-items: center; justify-content: center;
    gap: 60px;
  }
  .card {
    width: 900px; height: 500px; position: relative; overflow: hidden;
    box-shadow: 0 12px 30px rgba(0,0,0,.28);
  }
  /* Front */
  .card--front { background: var(--card-dark); }
  .front-brand {
    position: absolute; right: 70px; bottom: 70px;
    display: flex; align-items: center; gap: 22px;
  }
  .front-brand__mark { width: 46px; height: 46px; background: var(--brand-red); }
  .front-brand__name {
    color: var(--white); font-weight: 800; font-size: 64px; letter-spacing: 4px;
  }
  /* Back */
  .card--back { background: var(--card-light); color: var(--ink); }
  .contact-person { position: absolute; left: 60px; top: 60px; }
  .contact-person__first { color: var(--brand-red); font-weight: 300; font-size: 30px; line-height: 1.15; }
  .contact-person__last { color: var(--brand-red); font-weight: 700; font-size: 30px; line-height: 1.15; }
  .contact-person__role { color: var(--ink-soft); font-size: 15px; margin-top: 4px; }
  .contact-person__rule { width: 230px; height: 2px; background: var(--brand-red); margin-top: 14px; opacity: .7; }
  .contact-list { position: absolute; left: 60px; top: 250px; list-style: none; }
  .contact-list li {
    display: flex; align-items: center; gap: 14px;
    font-size: 16px; margin-bottom: 16px; color: var(--ink);
  }
  .contact-list strong { font-weight: 700; }
  .contact-list svg { width: 18px; height: 18px; flex: none; }
  .back-brand {
    position: absolute; right: 90px; top: 190px;
    display: flex; align-items: center; gap: 14px;
  }
  .back-brand__mark { width: 30px; height: 30px; background: var(--brand-red); }
  .back-brand__name { color: var(--ink); font-weight: 800; font-size: 40px; letter-spacing: 3px; }
  .address {
    position: absolute; right: 60px; bottom: 55px; text-align: right;
    font-size: 15px; line-height: 1.5; color: var(--ink);
  }
  .address__web { font-weight: 600; display: flex; align-items: center; justify-content: flex-end; gap: 8px; }
  .address__web svg { width: 16px; height: 16px; }
</style>
</head>
<body>
<main class="sheet">
  <section class="card card--front" aria-label="Frente do cartão">
    <div class="front-brand">
      <span class="front-brand__mark"></span>
      <span class="front-brand__name">VÉRTICE</span>
    </div>
  </section>

  <section class="card card--back" aria-label="Verso do cartão">
    <div class="contact-person">
      <p class="contact-person__first">Rafael Antunes</p>
      <p class="contact-person__last">Moreira</p>
      <p class="contact-person__role">Diretor Comercial</p>
      <div class="contact-person__rule"></div>
    </div>

    <ul class="contact-list">
      <li>
        <svg viewBox="0 0 24 24" fill="none" stroke="#9e1b1e" stroke-width="2" stroke-linecap="round" stroke-linejoin="round"><path d="M22 16.9v3a2 2 0 0 1-2.2 2 19.8 19.8 0 0 1-8.6-3.1 19.5 19.5 0 0 1-6-6A19.8 19.8 0 0 1 2.1 4.2 2 2 0 0 1 4.1 2h3a2 2 0 0 1 2 1.7c.1.9.4 1.8.7 2.7a2 2 0 0 1-.5 2.1L8 9.8a16 16 0 0 0 6 6l1.3-1.3a2 2 0 0 1 2.1-.4c.9.3 1.8.6 2.7.7a2 2 0 0 1 1.7 2z"/></svg>
        <span>+55 (11) <strong>3140-7285</strong></span>
      </li>
      <li>
        <svg viewBox="0 0 24 24" fill="none" stroke="#9e1b1e" stroke-width="2" stroke-linecap="round" stroke-linejoin="round"><rect x="6" y="2" width="12" height="20" rx="2"/><line x1="11" y1="18" x2="13" y2="18"/></svg>
        <span>+55 (11) <strong>97462-3018</strong></span>
      </li>
      <li>
        <svg viewBox="0 0 24 24" fill="none" stroke="#9e1b1e" stroke-width="2" stroke-linecap="round" stroke-linejoin="round"><rect x="3" y="5" width="18" height="14" rx="2"/><polyline points="3 7 12 13 21 7"/></svg>
        <span>contato@vertice.com.br</span>
      </li>
    </ul>

    <div class="back-brand">
      <span class="back-brand__mark"></span>
      <span class="back-brand__name">VÉRTICE</span>
    </div>

    <address class="address">
      <p class="address__web">www.vertice.com.br
        <svg viewBox="0 0 24 24" fill="#9e1b1e"><path d="M12 2a7 7 0 0 0-7 7c0 5 7 13 7 13s7-8 7-13a7 7 0 0 0-7-7zm0 9.5A2.5 2.5 0 1 1 12 6.5a2.5 2.5 0 0 1 0 5z"/></svg>
      </p>
      <p>Rua das Acácias, 215</p>
      <p>Vila Aurora - São Paulo - SP</p>
      <p>CEP 04512-090</p>
    </address>
  </section>
</main>
</body>
</html>
```